Australian Civil Construction, Quarry & Mining Services needs a business card

We need a business card designed for our Civil Construction, Quarry & Mining Services based in the country in Australia.
Our Company Brackley Earthworks provide innovate solutions for infrastructure, agricultural and mining (aggregate, sand, roadbase) industry.
We would like our business cards to be double sided
Front of card: black background or something that resembles our business colours. (it doesn't have to be black we are open to options)
- Company name - Brackley Earthworks
- Either our logo or some sort of icon/picture that resembles our business
- Website - https://brackleyearthworks.com.au/
- We will have a number of different names, positions descriptions, phone numbers and emails on separate cards for each of our managers/directors

```html
<!DOCTYPE html>
<html lang="en">
<head>
<meta charset="utf-8">
<title>Brackley Earthworks – Business Card</title>
<link rel="stylesheet" href="https://fonts.googleapis.com/css2?family=Archivo:wght@600;700&display=swap">
<style>
  :root {
    --orange: #f48120;
    --white: #ffffff;
    --ink: #111111;
    --backdrop: #e8e8e8;
  }
  html, body {
    margin: 0;
    padding: 0;
    width: 1200px;
    height: 1200px;
    overflow: hidden;
    background: var(--backdrop);
  }
  .canvas {
    position: relative;
    width: 1200px;
    height: 1200px;
  }
  .card {
    position: absolute;
    left: 333px;
    width: 534px;
    height: 306px;
    display: block;
  }
  .card--front { top: 222px; }
  .card--back { top: 671px; }
  .card-text {
    font-family: "Archivo", Arial, sans-serif;
    font-weight: 700;
    fill: var(--ink);
  }
  .brand-name { font-size: 15.5px; letter-spacing: 0.2px; }
  .person-name { font-size: 16px; letter-spacing: 0.3px; }
  .person-title { font-size: 6.6px; letter-spacing: 1.7px; fill: var(--orange); }
  .contact-line { font-size: 10.4px; font-weight: 600; }
  .band { fill: var(--orange); }
  .panel { fill: var(--white); }
  .brand-mark { fill: var(--orange); }
  .icon-disc { fill: var(--orange); }
  .icon-glyph { fill: var(--ink); }
  .icon-line { fill: none; stroke: var(--ink); stroke-width: 1; }
</style>
</head>
<body>
<main class="canvas">

  <!-- Front of card -->
  <svg class="card card--front" viewBox="0 0 445 255" role="img" aria-label="Business card front: Brackley Earthworks">
    <rect class="band" x="0" y="0" width="445" height="255"/>
    <polygon class="panel" points="0,36 410,36 445,122 445,220 35,220 0,132"/>
    <rect class="brand-mark" x="196" y="82" width="52" height="52"/>
    <text class="card-text brand-name" x="222.5" y="182" text-anchor="middle">BRACKLEY EARTHWORKS</text>
  </svg>

  <!-- Back of card -->
  <svg class="card card--back" viewBox="0 0 445 255" role="img" aria-label="Business card back: contact details">
    <rect class="band" x="0" y="0" width="445" height="255"/>
    <polygon class="panel" points="38,36 445,36 445,132 410,220 0,220 0,122"/>

    <text class="card-text person-name" x="120" y="75">CALLUM BRACKLEY</text>
    <text class="card-text person-title" x="120" y="85">CHIEF EXECUTIVE OFFICER</text>

    <!-- phone -->
    <g class="contact contact--phone">
      <circle class="icon-disc" cx="125" cy="117" r="8"/>
      <path class="icon-glyph" d="M121.3,112.6 l2,-0.6 1.3,2.9 -1.2,1 c0.6,1.3 1.5,2.3 2.8,2.9 l1,-1.2 2.9,1.3 -0.6,2 c-4.8,0.2 -8.5,-3.6 -8.2,-8.3z"/>
      <text class="card-text contact-line" x="139" y="121">03 5710 2864</text>
    </g>

    <!-- address -->
    <g class="contact contact--address">
      <circle class="icon-disc" cx="125" cy="143" r="8"/>
      <path class="icon-glyph" d="M125,138 a3.6,3.6 0 0 1 3.6,3.6 c0,2.6 -3.6,6.6 -3.6,6.6 s-3.6,-4 -3.6,-6.6 a3.6,3.6 0 0 1 3.6,-3.6z"/>
      <circle class="icon-disc" cx="125" cy="141.6" r="1.3"/>
      <text class="card-text contact-line" x="139" y="138">14 Kerrigan Lane, Tallowvale</text>
      <text class="card-text contact-line" x="139" y="151">Victoria 3731, Australia</text>
    </g>

    <!-- email -->
    <g class="contact contact--email">
      <circle class="icon-disc" cx="125" cy="166" r="8"/>
      <rect class="icon-glyph" x="120.5" y="162.8" width="9" height="6.4" rx="0.6"/>
      <polyline class="icon-line" stroke="#f48120" points="120.8,163.3 125,166.6 129.2,163.3" style="stroke: var(--orange)"/>
      <text class="card-text contact-line" x="139" y="170">admin@brackleyearthworks.com.au</text>
    </g>

    <!-- website -->
    <g class="contact contact--web">
      <circle class="icon-disc" cx="125" cy="191" r="8"/>
      <circle class="icon-line" cx="125" cy="191" r="4.4"/>
      <ellipse class="icon-line" cx="125" cy="191" rx="1.9" ry="4.4"/>
      <line class="icon-line" x1="120.6" y1="191" x2="129.4" y2="191"/>
      <text class="card-text contact-line" x="139" y="195">https://brackleyearthworks.com.au/</text>
    </g>
  </svg>

</main>
</body>
</html>
```